Flyer for The Quiet Bloom Gathering

I am launching my new offering in my business at an event next Sunday where I have a booth and need a flyer advertising the offering, so the flyer needs to stand out for other practitioners that will also be there on the day offering there services.
This flyer is also what I will use for marketing on social media as well as on the day of the event. See the link below to the offering
http://sarahlindqvist.com.au/quiet-bloom-gathering/

Target Market(s)

Women with body image issues - age range 25 - 65
Women with issues around food such as binge eating, emotional eating, eating disorders.

Industry/Entity Type

Health And Wellness

Font styles to use
Serif
Sans Serif
Script

Colors
f9d9e8
85cae6
cee9f5
fee18a
ffffff
eea4c8

Requirements
Must have
• Colours matching my overall website at sarahlindqvist.com.au - pinks, light blue, gold, white
• Imagery similiar to my Instagram, see below https://www.instagram.com/riverstonecarexy/
• - soft, warm, welcoming, nurturing, safe, inviting - see image on sales page for inspiration
• contact details
Should not have
• harsh dark colours or harsh lines

```html
<!DOCTYPE html>
<html lang="en">
<head>
<meta charset="utf-8">
<title>The Quiet Bloom Gathering – Flyer</title>
<link href="https://fonts.googleapis.com/css2?family=Lato:ital,wght@0,400;0,700;0,900;1,400;1,700&family=Kaushan+Script&display=swap" rel="stylesheet">
<style>
:root{
  --pink:#e0306f;
  --magenta:#d63a78;
  --violet:#7a4f8f;
  --navy:#1f4f7a;
  --teal:#1c93ae;
  --cyan:#3db5d3;
  --gold:#fee18a;
  --ink:#2a2a2a;
  --paper:#ffffff;
  --backdrop:#f1ece8;
}
*{box-sizing:border-box;margin:0;padding:0}
html,body{width:1200px;height:1200px;overflow:hidden;background:var(--backdrop)}
body{font-family:"Lato",sans-serif;color:var(--ink);position:relative}
.flyer{position:absolute;left:188px;top:20px;width:824px;height:1160px;background:var(--paper);overflow:hidden;box-shadow:0 2px 10px rgba(0,0,0,.08)}
.brand{position:absolute;top:32px;left:0;right:0;text-align:center}
.brand-name{font-weight:400;font-size:40px;letter-spacing:1px;color:var(--magenta);line-height:1}
.brand-rule{width:250px;height:2px;background:var(--gold);margin:8px auto 6px}
.brand-tagline{font-weight:700;font-size:11px;color:var(--cyan)}
.hero{position:absolute;left:0;top:112px;width:824px;height:370px}
.title{position:absolute;top:488px;left:0;right:0;text-align:center;font-family:"Kaushan Script",cursive;font-size:58px;line-height:1.1;
  background:linear-gradient(90deg,var(--pink) 0%,var(--magenta) 30%,var(--violet) 50%,var(--navy) 65%,var(--teal) 100%);
  -webkit-background-clip:text;background-clip:text;color:transparent}
.intro{position:absolute;top:582px;left:60px;right:60px;text-align:center;font-size:13px;line-height:21px}
.intro h2{font-size:15px;font-weight:900;letter-spacing:.2px;margin-bottom:1px}
.hl{color:var(--pink);font-weight:700}
.intro .ask{color:var(--cyan);font-style:italic;font-weight:700;font-size:15px;line-height:21px}
.columns{position:absolute;top:818px;left:18px;right:30px;display:flex;gap:28px;font-size:11.5px;line-height:15px}
.col{flex:1}
.point{position:relative;padding-left:14px;margin-bottom:17px;text-align:justify}
.point::before{content:"";position:absolute;left:0;top:2px;width:5px;height:11px;background:var(--cyan)}
.point.pink::before{background:var(--pink)}
.lead-pink{color:var(--pink);font-style:italic}
.lead-cyan{color:var(--cyan);font-style:italic}
.perks{list-style:none;margin:16px 0 14px 14px}
.perks li{position:relative;padding-left:14px;margin-bottom:5px}
.perks li::before{content:"";position:absolute;left:1px;top:4px;width:6px;height:6px;border-radius:50%;background:var(--pink)}
.price{color:var(--cyan);font-weight:700;font-size:13px}
.cta{position:absolute;top:1030px;left:185px;width:460px;height:62px}
.cta span{position:absolute;inset:0;display:flex;align-items:center;justify-content:center;font-weight:700;font-size:36px;color:#fff;text-shadow:0 1px 2px rgba(0,0,0,.25)}
.contact{position:absolute;top:1102px;left:170px;width:486px;display:flex;align-items:center;gap:8px;font-size:12px}
.contact .phone{font-weight:700;font-size:16px;margin-right:10px}
.contact svg{flex:none}
.socials{display:flex;gap:10px;margin-left:auto}
.socials i{display:block;width:18px;height:18px;border-radius:50%;background:var(--cyan)}
.gold-rule{position:absolute;top:1130px;left:170px;width:486px;height:5px;background:var(--gold)}
</style>
</head>
<body>
<main class="flyer">
  <header class="brand">
    <div class="brand-name">Sarah Lindqvist</div>
    <div class="brand-rule"></div>
    <div class="brand-tagline">Find Gentle Peace with Your Body and Your Plate</div>
  </header>

  <svg class="hero" viewBox="0 0 824 370" role="img" aria-label="Photo of a woman stretching her arms upward by the sea at a soft pastel sunset">
    <defs>
      <linearGradient id="sky" x1="0" y1="0" x2="0" y2="1">
        <stop offset="0" stop-color="#c9ccd6"/>
        <stop offset=".35" stop-color="#e9c2b4"/>
        <stop offset=".55" stop-color="#f2b99a"/>
        <stop offset=".72" stop-color="#c9a7a8"/>
        <stop offset=".82" stop-color="#556b83"/>
        <stop offset="1" stop-color="#8a9bb0"/>
      </linearGradient>
    </defs>
    <path d="M0 18 Q60 8 130 14 T260 10 T420 18 T600 8 T824 14 L824 345 Q700 360 560 352 T300 356 T0 348 Z" fill="url(#sky)"/>
  </svg>

  <h1 class="title">The Quiet Bloom Gathering</h1>

  <section class="intro">
    <h2>IT'S TIME TO MAKE A COMMITMENT….</h2>
    <p>It's time for <span class="hl">YOU</span>, to <span class="hl">SHOW UP</span> for <span class="hl">YOU</span>…..</p>
    <p>It's time to truly let go…….and finally heal, and find the peace that you so long for…</p>
    <p>You deserve to feel the freedom that comes with truly loving and accepting your body.</p>
    <p>You deserve the freedom that comes with experiencing a deeper trusting</p>
    <p>connection with your body, where you feel safe, at home.</p>
    <p>Can you even imagine a whole day that you didn't hate your body,</p>
    <p>you didn't fight with food, and you felt peaceful and at home with your body?</p>
    <p class="ask">Can you love the part of you, that hates your body?<br>You can't heal something you hate.</p>
  </section>

  <section class="columns">
    <div class="col">
      <p class="point"><span class="lead-pink">It's time to show up for YOU</span>, consistently, every week, and do the work, once and for all. No more games, no more half in on YOU…. You deserve better than a life contained in the mental prison of body hatred.</p>
      <p class="point pink"><span class="lead-cyan">Are you truly ready to make the commitment?</span><br>How would it feel to be able to say, <em>"I am free to love and accept my body"</em>, and <em>"I am free, connected and at peace to my body"</em>?</p>
      <p class="point"><span class="lead-pink">I am inviting 10 women only into this six-week healing experience,</span> as I personally know, that when we share our stories, it opens our hearts for other people to share their stories. It gives us the sense we are not alone in our journey's.</p>
    </div>
    <div class="col">
      <p class="point pink">The women that come on this six-week journey will receive;</p>
      <ul class="perks">
        <li>One 90mins one on one coaching session with me (which for the women that have attended the Friday circle previously, can be done before this healing circle begins);</li>
        <li>Private Online Group to continue support outside of the circle</li>
        <li>Homework outside of circle to support your healing</li>
        <li>Journal and other small gifts weekly</li>
      </ul>
      <p class="point pink">The financial investment in <span class="hl">YOU</span>, is <span class="price">$XX</span> for the six weeks. For the women that have attended the Friday night, Soft Ground Sister Circle, you will receive a discount of <span class="hl">$100</span>, taking the price to <span class="price">$XX</span>.</p>
    </div>
  </section>

  <div class="cta">
    <svg width="460" height="62" viewBox="0 0 460 62" aria-hidden="true">
      <path d="M8 6 Q120 0 240 4 T456 2 L448 30 L458 50 Q300 60 180 56 T2 60 L10 38 Z" fill="var(--pink)"/>
    </svg>
    <span>Are You Ready?</span>
  </div>

  <footer class="contact">
    <svg width="20" height="16" viewBox="0 0 20 16" aria-hidden="true"><path d="M2 6 Q10 -1 18 6 L15 8 L13 5 H7 L5 8 Z M5 9 H15 L17 15 H3 Z" fill="var(--cyan)"/></svg>
    <span class="phone">0400 555 217</span>
    <svg width="18" height="14" viewBox="0 0 18 14" aria-hidden="true"><rect x="1" y="1" width="16" height="12" fill="none" stroke="var(--cyan)" stroke-width="1.6"/><path d="M1 1 L9 8 L17 1" fill="none" stroke="var(--cyan)" stroke-width="1.6"/></svg>
    <span>sarah@sarahlindqvist.com.au</span>
    <div class="socials" aria-label="Social channels"><i></i><i></i><i></i><i></i></div>
  </footer>
  <div class="gold-rule"></div>
</main>
</body>
</html>
```